The Tidy Hound - Dog Training Business Card Design

I need a business card design for a new dog training company based in Cronulla NSW called The Tidy Hound. I run puppy pre school classes, adult dog classes and do one on one training in the person's home.
I have studied for 2 years and use positive reinforcement training methods based on how dogs learn. I believe in communicating with our dogs what we want them to do rather than punish them for behaviours we don't like. I would like to see designs that use the colours that are used in my logo (please see attached)
I would like a simple and classic looking design. I don't want cartoon images of dogs or any animal images or drawings on the card. I have created my logo with this mindset. I am open to the subtle use of a dog's tail, paws or paw print.

Target Market(s)

high end area which is why I want a classic looking design
adults aged 25 and over

Industry/Entity Type

Dog Training

Contact Information for Business Card

Marcy Tellwin
ORBIS Trained Professional Dog Trainer
www.thetidyhound-example.com.au
0491837265
marcy@thetidyhound-example.com.au

Font styles to use
Sans Serif

Colors
ffffff
86cae6
757575

Requirements
Must have
• Logo - I am trying to attach my logo and colour palette but it won't allow me. I will contact the company and upload ASAP.
Should not have
• images of dogs or cartoon drawings

```html
<!DOCTYPE html>
<html lang="en">
<head>
<meta charset="utf-8">
<title>The Tidy Hound – Business Card</title>
<link href="https://fonts.googleapis.com/css2?family=Open+Sans:wght@300;400;600&display=swap" rel="stylesheet">
<style>
  :root {
    --page-bg: #e4e6e8;
    --sky: #b7d5ec;
    --brand-blue: #86cae6;
    --brand-grey: #757575;
    --logo-grey: #a8a59d;
    --text-dark: #4a4a4a;
    --white: #ffffff;
    --card-white: #f7f7f7;
    --card-grey: #e3e3e3;
    --map-tone: #d9d9d9;
  }
  * { box-sizing: border-box; margin: 0; padding: 0; }
  html, body { width: 1200px; height: 964px; overflow: hidden; }
  body {
    background: var(--page-bg);
    font-family: "Open Sans", Arial, sans-serif;
    position: relative;
  }
  .card {
    position: absolute;
    left: 220px;
    width: 760px;
    height: 434px;
    box-shadow: 0 10px 28px rgba(0,0,0,0.18);
    overflow: hidden;
  }
  /* Front */
  .card--front { top: 40px; background: var(--sky); }
  .front-brand {
    position: absolute; left: 0; right: 0; top: 150px;
    text-align: center; color: var(--white);
  }
  .front-brand .brand-name {
    font-size: 64px; font-weight: 300; letter-spacing: 1px; line-height: 1;
  }
  .front-brand .brand-tagline {
    margin-top: 14px; font-size: 15px; font-weight: 400; letter-spacing: 4px;
  }
  /* Back */
  .card--back {
    top: 490px;
    background: radial-gradient(ellipse at 45% 60%, var(--white) 0%, var(--card-white) 45%, var(--card-grey) 100%);
  }
  .map-area {
    position: absolute; left: 40px; top: 20px; width: 680px; height: 360px;
    background: radial-gradient(ellipse at center, rgba(200,200,200,0.35) 0%, rgba(220,220,220,0.15) 55%, rgba(255,255,255,0) 75%);
  }
  .back-brand {
    position: absolute; left: 40px; top: 150px; width: 330px; color: var(--logo-grey);
  }
  .back-brand .brand-name {
    font-size: 46px; font-weight: 300; line-height: 1; letter-spacing: 0.5px;
  }
  .back-brand .brand-tagline {
    margin-top: 12px; font-size: 12px; letter-spacing: 3.5px; font-weight: 400;
  }
  .divider {
    position: absolute; left: 392px; top: 70px; width: 2px; height: 196px;
    background: var(--text-dark);
  }
  .contact { position: absolute; left: 420px; top: 64px; color: var(--text-dark); }
  .contact .person-name { font-size: 24px; font-weight: 600; letter-spacing: 0.5px; }
  .contact .person-role { font-size: 17px; font-weight: 400; letter-spacing: 0.5px; margin-top: 2px; }
  .contact-row { display: flex; align-items: center; gap: 14px; margin-top: 16px; }
  .contact-row .icon {
    width: 40px; height: 40px; border-radius: 50%; background: var(--brand-grey);
    display: flex; align-items: center; justify-content: center; flex-shrink: 0;
  }
  .contact-row .lines { font-size: 15px; line-height: 1.35; }
  .address {
    position: absolute; left: 0; right: 0; bottom: 46px; text-align: center;
    font-size: 18px; color: var(--text-dark); padding-left: 120px;
  }
</style>
</head>
<body>

  <section class="card card--front" aria-label="Business card front">
    <div class="front-brand">
      <div class="brand-name">The Tidy Hound</div>
      <div class="brand-tagline">POSITIVE TRAINING SPECIALIST</div>
    </div>
  </section>

  <section class="card card--back" aria-label="Business card back">
    <div class="map-area" role="img" aria-label="Faint world map in the background"></div>

    <div class="back-brand">
      <div class="brand-name">The Tidy Hound</div>
      <div class="brand-tagline">POSITIVE TRAINING SPECIALIST</div>
    </div>

    <div class="divider"></div>

    <div class="contact">
      <div class="person-name">MARCY TELLWIN</div>
      <div class="person-role">GENERAL MANAGER</div>

      <div class="contact-row">
        <span class="icon">
          <svg width="20" height="20" viewBox="0 0 24 24" aria-hidden="true">
            <path fill="#ffffff" d="M6.6 10.8c1.4 2.8 3.8 5.1 6.6 6.6l2.2-2.2c.3-.3.7-.4 1-.2 1.1.4 2.3.6 3.6.6.6 0 1 .4 1 1V20c0 .6-.4 1-1 1C10.6 21 3 13.4 3 4c0-.6.4-1 1-1h3.5c.6 0 1 .4 1 1 0 1.3.2 2.5.6 3.6.1.3 0 .7-.2 1L6.6 10.8z"/>
          </svg>
        </span>
        <div class="lines">
          <div>0491837265</div>
          <div>0491837265</div>
        </div>
      </div>

      <div class="contact-row">
        <span class="icon">
          <svg width="22" height="20" viewBox="0 0 24 22" aria-hidden="true">
            <rect x="2" y="2" width="20" height="13" rx="1" fill="none" stroke="#ffffff" stroke-width="2"/>
            <rect x="9" y="16" width="6" height="3" fill="#ffffff"/>
            <rect x="6" y="19" width="12" height="2" fill="#ffffff"/>
          </svg>
        </span>
        <div class="lines">
          <div>marcy@thetidyhound-example.com.au</div>
          <div>www.thetidyhound-example.com.au</div>
        </div>
      </div>
    </div>

    <div class="address">14 Kingsway, Cronulla NSW 2230</div>
  </section>

</body>
</html>
```